Flyer Brightfork Outings

I need two flyers with similar designs, one for the Brightfork Outings Sevilla brand and another for the Brightfork Outings Marbella & Estepona brand, in which the most important characteristics of some of the best products on each website appear with their prices.

The RRSS and contact information, website and QR must also appear.

Target Market(s)

Tourists visiting South of Spain

Industry/Entity Type

Tourism

Font styles to use
Other font styles liked:
• montserrat

Colors
FFC000
F8CF3A
FAE287
FDF2CF
FEFAEE
F0912C
F2A743
F7CA91
FBE8D2
FDF5EE

Requirements
Must have
• Activities listed on the website, social media info, contact information, brief descriptions...
Nice to have
• Back side for both flyers has to be the same, with something catchy for people to grab the flyer and book any activity with us

```html
<!DOCTYPE html>
<html lang="en">
<head>
<meta charset="utf-8">
<title>Brightfork Outings – Flyers</title>
<link rel="stylesheet" href="https://fonts.googleapis.com/css2?family=Bebas+Neue&family=Dancing+Script:wght@600&family=Poppins:wght@400;500;600;700&display=swap">
<style>
:root{
  --stage:#b5b5b5;
  --paper:#ffffff;
  --panel:#4a4646;
  --orange:#f2a01e;
  --ink:#2f2f2f;
  --muted:#555;
  --line:#e2c68a;
}
*{box-sizing:border-box;margin:0;padding:0}
html,body{width:1200px;height:841px;overflow:hidden}
body{background:var(--stage);font-family:'Poppins',sans-serif;color:var(--ink);position:relative}
.flyer{position:absolute;top:104px;width:487px;height:631px;background:var(--paper);overflow:hidden}
.flyer--marbella{left:74px}
.flyer--sevilla{left:636px}
.abs{position:absolute}
.panel{position:absolute;top:0;right:0;background:var(--panel)}
.brand{position:absolute;left:33px;top:38px;display:flex;align-items:center;gap:9px}
.brand__mark{width:14px;height:14px;background:var(--orange)}
.brand__name{font-family:'Bebas Neue',sans-serif;font-size:23px;line-height:.92;color:var(--panel);letter-spacing:.3px}
.kicker{font-family:'Poppins',sans-serif;font-weight:500;color:#fff;font-size:17px;letter-spacing:6px;line-height:1}
.hl-box{background:var(--orange);color:#fff;font-family:'Bebas Neue',sans-serif;line-height:1;padding:2px 5px 0}
.hl-orange{font-family:'Bebas Neue',sans-serif;color:var(--orange);line-height:1}
.script{font-family:'Dancing Script',cursive;color:var(--orange)}
.frame{position:absolute;background:var(--orange)}
.photo{position:absolute;border:2px solid #fff}
.thumb{position:absolute;border:1.5px solid var(--orange)}
.item{position:absolute;text-align:center;font-weight:600;font-size:7.4px;line-height:1.2;color:#333}
.price{display:inline-block;margin-top:2px;background:var(--orange);color:#fff;font-size:7px;font-weight:700;padding:0 9px;clip-path:polygon(0 0,100% 0,94% 50%,100% 100%,0 100%,6% 50%)}
.welcome{font-weight:700;color:var(--orange);line-height:1.25;text-transform:uppercase}
.body-copy{color:#fff;font-weight:400}
.feature{position:absolute;text-align:center;font-size:6.3px;line-height:1.25;color:#222}
.feature b{display:block;font-weight:700}
.feature__icon{width:22px;height:22px;border:1.5px solid var(--orange);border-radius:50%;margin:0 auto 6px;background:#fdf2cf}
.divider{position:absolute;border-left:1px dashed var(--line)}
.contact-label{position:absolute;left:32px;top:570px;font-size:8.6px;color:var(--orange);font-weight:400}
.contact-label b{font-weight:700}
.phone{position:absolute;left:32px;top:585px;display:flex;align-items:center;gap:7px;font-size:15px;font-weight:600;color:#333}
.email{position:absolute;left:225px;top:571px;display:flex;align-items:center;gap:8px;font-size:10.4px;color:#333}
.web{position:absolute;left:219px;top:585px;width:268px;height:13px;background:var(--orange);color:#fff;font-size:7.6px;font-weight:700;letter-spacing:2.6px;line-height:13px;padding-left:7px}
.list{position:absolute;list-style:none;font-size:6.6px;font-weight:600;color:#333}
.list li{display:flex;align-items:center;gap:5px;margin-bottom:4.4px}
.list li::before{content:"";width:5px;height:5px;border-radius:50%;background:var(--orange)}
.cell{position:absolute;display:flex;gap:8px;align-items:flex-start}
.cell .feature__icon{width:26px;height:26px;margin:6px 0 0;flex:none}
.cell__text{font-size:7.4px;line-height:1.2;color:#222}
.cell__text b{display:block;font-size:9.8px;font-weight:700}
</style>
</head>
<body>

<!-- Marbella & Estepona flyer -->
<section class="flyer flyer--marbella">
  <div class="panel" style="width:258px;height:481px"></div>

  <div class="brand">
    <span class="brand__mark"></span>
    <span class="brand__name">Brightfork<br>Outings</span>
  </div>

  <div class="abs kicker" style="left:254px;top:34px">ENJOY</div>
  <div class="abs hl-box" style="left:255px;top:54px;font-size:25px">MARBELLA &amp; ESTEPONA</div>
  <div class="abs script" style="left:257px;top:78px;font-size:15px">with</div>
  <div class="abs hl-orange" style="left:258px;top:90px;font-size:26px">BRIGHTFORK OUTINGS</div>

  <div class="frame" style="left:32px;top:118px;width:197px;height:171px"></div>
  <div class="photo" role="img" aria-label="Evening view of whitewashed hillside buildings lit up on the coast" style="left:37px;top:124px;width:418px;height:159px;background:linear-gradient(180deg,#8a6fb5 0%,#b79ab0 30%,#6c4f6e 55%,#3e3140 100%)"></div>

  <div class="thumb" role="img" aria-label="Glasses of sangria with tapas on a terrace" style="left:44px;top:299px;width:70px;height:54px;background:linear-gradient(#b7c7d6,#5a5f6e)"></div>
  <div class="item" style="left:34px;top:356px;width:90px">Sangria Tasting<br>&amp; Tapas<br><span class="price">€30.00</span></div>
  <div class="thumb" role="img" aria-label="Chef cooking paella in a kitchen" style="left:130px;top:299px;width:70px;height:54px;background:linear-gradient(#c9a47a,#59636a)"></div>
  <div class="item" style="left:120px;top:356px;width:90px">Paella<br>Showcooking<br><span class="price">€45.00</span></div>
  <div class="thumb" role="img" aria-label="Friends sharing sangria at a table" style="left:44px;top:397px;width:70px;height:54px;background:linear-gradient(#9b8876,#4a3c3a)"></div>
  <div class="item" style="left:34px;top:452px;width:90px">Sangria<br>Tasting<br><span class="price">€20.00</span></div>
  <div class="thumb" role="img" aria-label="Picnic basket and blanket by the sea" style="left:130px;top:397px;width:70px;height:54px;background:linear-gradient(#a9c1d6,#7d8aa3)"></div>
  <div class="item" style="left:120px;top:452px;width:90px">Picnic Brunch<br>Experience<br><span class="price">€35.00</span></div>

  <div class="abs welcome" style="left:284px;top:304px;font-size:10.6px">Welcome to<br>Marbella &amp; Estepona</div>
  <p class="abs body-copy" style="left:246px;top:345px;width:206px;font-size:9.2px;line-height:10.5px">Get ready for an epic picnic experience right in the heart of Marbella &amp; Estepona’s beauty! Picture this: you, your crew, and a spread of the yummiest treats – think artisanal cheeses, crusty bread, and fresh local goodies. Plus, we’ve got the drinks covered, so you can kick back, relax, and soak in those chill vibes. It’s all about good food, good company, and making memories in Marbella &amp; Estepona’s stunning scenery. Let’s picnic like never before!</p>

  <div class="feature" style="left:34px;top:500px;width:76px"><div class="feature__icon" role="img" aria-label="Paella pan icon"></div><b>Delicious Paella</b>There is no Spanish dish more iconic than Paella!</div>
  <div class="divider" style="left:112px;top:505px;height:55px"></div>
  <div class="feature" style="left:116px;top:500px;width:86px"><div class="feature__icon" role="img" aria-label="Sangria glass icon"></div><b>Fresh Sangria</b>Who could resist a cold, refreshing, delicious glass of sangria?</div>
  <div class="divider" style="left:211px;top:505px;height:55px"></div>
  <div class="feature" style="left:214px;top:500px;width:84px"><div class="feature__icon" role="img" aria-label="Local produce icon"></div><b>Local Food</b>Experience true Spanish cuisine with fresh, local ingredients.</div>
  <div class="divider" style="left:304px;top:505px;height:55px"></div>
  <div class="feature" style="left:308px;top:500px;width:72px"><div class="feature__icon" role="img" aria-label="Team with stars icon"></div><b>Best staff</b>Each experience is guided by our fun, knowledgeable team.</div>
  <div class="divider" style="left:400px;top:505px;height:55px"></div>
  <div class="feature" style="left:402px;top:500px;width:58px"><div class="feature__icon" role="img" aria-label="Picnic basket icon"></div><b>Go picnic</b>Get ready for an epic picnic experience.</div>

  <div class="contact-label"><b>CONTACT US</b> FOR MORE INFORMATION</div>
  <div class="phone"><svg width="12" height="12" viewBox="0 0 24 24"><circle cx="12" cy="12" r="12" fill="#f2a01e"/><path d="M8 6.5l2 .2 1 3-1.4 1.2a8 8 0 0 0 3.5 3.5l1.2-1.4 3 1 .2 2c-.2.8-1 1.3-1.8 1.2C10.8 16.6 7.4 13.2 6.8 8.3 6.7 7.5 7.2 6.7 8 6.5z" fill="#fff"/></svg>555 0142 0199</div>
  <div class="email"><svg width="10" height="10" viewBox="0 0 24 24"><circle cx="12" cy="12" r="12" fill="#f2a01e"/><rect x="6" y="8" width="12" height="8" fill="none" stroke="#fff" stroke-width="1.6"/><path d="M6 8l6 5 6-5" fill="none" stroke="#fff" stroke-width="1.6"/></svg>info@brightforkoutings.com</div>
  <div class="web">www.brightforkoutings.com</div>
</section>

<!-- Sevilla flyer -->
<section class="flyer flyer--sevilla">
  <div class="panel" style="width:272px;height:428px"></div>

  <div class="brand">
    <span class="brand__mark"></span>
    <span class="brand__name">Brightfork<br>Outings</span>
  </div>

  <div class="abs kicker" style="left:255px;top:36px">EXPLORING</div>
  <div class="abs hl-box" style="left:256px;top:53px;font-size:31px;padding:1px 7px 0">SPAIN ONE BITE</div>
  <div class="abs hl-orange" style="left:256px;top:88px;font-size:32px">AT A TIME</div>

  <div class="frame" style="left:32px;top:118px;width:183px;height:163px"></div>
  <div class="photo" role="img" aria-label="Group of friends laughing at a rooftop table with drinks" style="left:37px;top:123px;width:419px;height:153px;background:linear-gradient(180deg,#c9c4ba 0%,#9c8f82 45%,#5e5650 100%)"></div>

  <div class="thumb" role="img" aria-label="Flamenco dancers on a blue-lit stage" style="left:40px;top:300px;width:67px;height:51px;background:linear-gradient(#2f47b8,#1b2358)"></div>
  <div class="item" style="left:28px;top:354px;width:90px;font-size:6.6px">Flamenco<br>Tour and Show<br><span class="price">€30.00</span></div>
  <div class="thumb" role="img" aria-label="Chef cooking paella in a kitchen" style="left:128px;top:300px;width:67px;height:51px;background:linear-gradient(#c9a47a,#59636a)"></div>
  <div class="item" style="left:116px;top:354px;width:90px;font-size:6.6px">Paella<br>Showcooking<br><span class="price">€45.00</span></div>
  <div class="thumb" role="img" aria-label="Friends sharing sangria at a table" style="left:40px;top:390px;width:67px;height:51px;background:linear-gradient(#9b8876,#4a3c3a)"></div>
  <div class="item" style="left:28px;top:444px;width:90px;font-size:6.6px">Sangria<br>Tasting<br><span class="price">€20.00</span></div>
  <div class="thumb" role="img" aria-label="Colourful market stalls with shoppers" style="left:128px;top:390px;width:67px;height:51px;background:linear-gradient(#d0603f,#7a3140)"></div>
  <div class="item" style="left:116px;top:444px;width:90px;font-size:6.6px">Triana Market<br>Tapas Tour<br><span class="price">€35.00</span></div>
  <div class="thumb" role="img" aria-label="Plate of pastries and red drinks" style="left:40px;top:480px;width:67px;height:51px;background:linear-gradient(#c43c4c,#e9e0da)"></div>
  <div class="item" style="left:28px;top:533px;width:90px;font-size:6.6px">Ugly Food<br>Tour<br><span class="price">€35.00</span></div>

  <ul class="list" style="left:128px;top:489px">
    <li>Wine Tasting</li><li>Food Trips</li><li>Flamenco Experience</li><li>Olive Oil Tasting</li>
  </ul>

  <div class="abs" style="left:236px;top:301px;font-size:9px;font-weight:700;color:var(--orange);line-height:1.15">Gastronomic experiences<br>with a breathtaking view of Sevilla:</div>
  <div class="abs" style="left:236px;top:326px;font-size:8.4px;color:#fff">GREAT FOOD &nbsp;|&nbsp; STUNNING VIEW &nbsp;|&nbsp; BEST CHOICE.</div>
  <div class="abs welcome" style="left:236px;top:352px;font-size:9.6px">Welcome to Sevilla</div>
  <p class="abs body-copy" style="left:236px;top:372px;width:200px;font-size:8.3px;line-height:9.6px">Enjoy a special paella dining experience on one of the most exclusive rooftops in Seville. Savor delicious appetizers, local wine, and a fresh paella that make for a truly memorable meal.</p>

  <div class="cell" style="left:221px;top:449px;width:122px"><div class="feature__icon" role="img" aria-label="Paella pan icon"></div><div class="cell__text"><b>Delicious Paella</b>There is no Spanish dish more iconic than Paella!</div></div>
  <div class="divider" style="left:343px;top:444px;height:120px"></div>
  <div class="cell" style="left:349px;top:449px;width:130px"><div class="feature__icon" role="img" aria-label="Team with stars icon"></div><div class="cell__text"><b>Best staff</b>Each experience is guided by our fun, knowledgeable team.</div></div>
  <div class="abs" style="left:221px;top:504px;width:262px;border-top:1px dashed var(--line)"></div>
  <div class="cell" style="left:221px;top:509px;width:122px"><div class="feature__icon" role="img" aria-label="Local produce icon"></div><div class="cell__text"><b>Local Food</b>Experience true Spanish cuisine with fresh, local ingredients.</div></div>
  <div class="cell" style="left:349px;top:509px;width:130px"><div class="feature__icon" role="img" aria-label="Sangria glass icon"></div><div class="cell__text"><b>Fresh Sangria</b>Who could resist a cold, refreshing, delicious glass of sangria?</div></div>

  <div class="contact-label"><b>CONTACT US</b> FOR MORE INFORMATION</div>
  <div class="phone"><svg width="12" height="12" viewBox="0 0 24 24"><circle cx="12" cy="12" r="12" fill="#f2a01e"/><path d="M8 6.5l2 .2 1 3-1.4 1.2a8 8 0 0 0 3.5 3.5l1.2-1.4 3 1 .2 2c-.2.8-1 1.3-1.8 1.2C10.8 16.6 7.4 13.2 6.8 8.3 6.7 7.5 7.2 6.7 8 6.5z" fill="#fff"/></svg>555 0142 0199</div>
  <div class="email"><svg width="10" height="10" viewBox="0 0 24 24"><circle cx="12" cy="12" r="12" fill="#f2a01e"/><rect x="6" y="8" width="12" height="8" fill="none" stroke="#fff" stroke-width="1.6"/><path d="M6 8l6 5 6-5" fill="none" stroke="#fff" stroke-width="1.6"/></svg>info@brightforkoutings.com</div>
  <div class="web">www.brightforkoutings.com</div>
</section>

</body>
</html>
```